Reaching the Root: Reasoning in Clinical Choice-Making

I'd like a cover that looks like it would fit on the shelf next to "The Symptom Mirage" by Harold Vintner, "The Fall of Forgetting" by Carl Mortenson, "Meal Mend" by Neil Forsby, "The Energy Renewal Plan" by Owen Prichardson or "The Gland Renewal Plan" by the same or "The Cortex Renewal Plan" by the same ... either text only (with some interesting fonts that make the title stand out, and the subtitle smaller) or a relevant image, though I'm not entirely sure what that would be since this is a book about big-picture medical decision making.
Author name is Dr Miriam Oakhurst, NMD
I'll eventually request an e-book, paperback, and audio cover from the winner...

Target Market(s)

practicing physicians

Industry/Entity Type

medicine

Requirements
Must have
• look similar to other books in the genre

```html
<!DOCTYPE html>
<html lang="en">
<head>
<meta charset="utf-8">
<title>Reaching the Root — Book Cover</title>
<link href="https://fonts.googleapis.com/css2?family=Old+Standard+TT:wght@400;700&display=swap" rel="stylesheet">
<style>
  :root {
    --stage: #4d4d4d;
    --paper: #f7f4f0;
    --navy: #0f1f40;
    --gold: #9a7b3a;
    --rule: #8a94a8;
  }
  * { margin: 0; padding: 0; box-sizing: border-box; }
  html, body {
    width: 1200px;
    height: 2854px;
    overflow: hidden;
    background: var(--stage);
  }
  .cover {
    position: absolute;
    left: 139px;
    top: 736px;
    width: 923px;
    height: 1382px;
    background: var(--paper);
    box-shadow: 0 20px 60px rgba(0,0,0,0.45);
    font-family: "Old Standard TT", Georgia, serif;
    color: var(--navy);
  }
  .cover > * {
    position: absolute;
    left: 0;
    width: 100%;
    text-align: center;
  }
  .title-lead {
    top: 40px;
    font-size: 142px;
    line-height: 1;
    letter-spacing: 1px;
  }
  .title-key {
    top: 228px;
    font-size: 300px;
    line-height: 1;
    color: var(--gold);
    letter-spacing: 4px;
  }
  .subtitle-lead {
    top: 504px;
    display: flex;
    align-items: center;
    justify-content: center;
    gap: 22px;
    font-size: 52px;
    line-height: 1;
  }
  .subtitle-lead .rule {
    display: block;
    width: 170px;
    height: 1px;
    background: var(--rule);
  }
  .subtitle-key {
    top: 572px;
    font-size: 122px;
    font-weight: 700;
    line-height: 1;
    letter-spacing: 1px;
  }
  .subtitle-tail {
    top: 694px;
    font-size: 42px;
    line-height: 1;
    letter-spacing: 9px;
  }
  .compass-art {
    top: 779px;
    left: 236px;
    width: 450px;
    height: 450px;
    border-radius: 50%;
    background: radial-gradient(circle, #e9e3d8 0%, #eeeae4 55%, var(--paper) 72%);
  }
  .author {
    top: 1258px;
    font-size: 50px;
    line-height: 1;
  }
</style>
</head>
<body>
  <main class="cover">
    <h1 class="title-lead">Reaching the</h1>
    <div class="title-key">ROOT</div>
    <p class="subtitle-lead"><span class="rule"></span>Reasoning in<span class="rule"></span></p>
    <p class="subtitle-key">CLINICAL</p>
    <p class="subtitle-tail">Choice-Making</p>
    <div class="compass-art" role="img" aria-label="Navy and gold compass rose with N, E, S, W markers"></div>
    <p class="author">Dr Miriam Oakhurst, NMD</p>
  </main>
</body>
</html>
```